energy rating company

Web Design graphics and layout only

To create two pages for the website. First the home page and the second is the design for the job board for our clients use after login. I have attached files that explain in detail what the pages should have and the purpose/desires of each object. Please read these thoroughly.

The webpages need to be clean, professional, easy on the eye, obvious in all its buttons and functions with a strong call to action on the home page and branding and clean, great and obvious looking buttons and very simple but dynamic as well. We wish to be seen as contemporary.

Business Concept

Our business concept is simple, to build a website whereby our clients will be able to upload jobs for energy raters to quote on and subsequent complete the work if their quote is selected. To link energy ratings that are required with energy raters via our website. Similarly to the varlo website, jobs will be “advertised” on the job board and raters will select which jobs they wish to quote for.

I have attached a Word document explaining all the parts of the website and another word document showing what we are sort of after and a excel spreadsheet as well. Please read these in conjunction with this brief!
Updates

Dear All

I have submitted with my brief a word doc and excel spreadsheet of the two pages I want created.  However this is not the layout or design I want, I only put it together so that you will need to know what is required on each page.  Feel free to change and redesign it all.

Also the second page does not require the "process" logo or any other menu items except the first five being Home, How it works, About Us, testimonials and Contact us as per the home page.

We also are looking for something very professional and very clean.  It should be very easy to see exactly what you are looking for.

I will also extend the deadline for new designers!!  I am excited to see your talents!!

Thanks

I have increase budget and posted a note saying feel free to change all the details layout etc on my brief just include everything!!! 

Wanting a professional corporate look...

Want a professional corporate look

We have changed our minds and you we no longer require the process to be on the home page.

Thanks

Target Market(s)

Target Market

Home Inspection Companies
Pest Inspection Companies
Residential home buyers/sellers
Real Estate companies

Industry/Entity Type

It Company

Number of Pages Required

1 page

Requirements
Must have
• Colours and Styles

• The website should be mainly white as I believe it is seen as clean and simple with colour from the logos, but can be swayed if it projects the image we are after.

• It should be obvious and process orientated and I do believe symbols, pictures, etc should replace words where possible.

```html
<!DOCTYPE html>
<html lang="en">
<head>
<meta charset="utf-8">
<title>lumora australia – Energy Rating Quotes</title>
<link rel="stylesheet" href="https://fonts.googleapis.com/css2?family=Play:wght@400;700&family=PT+Sans:ital,wght@0,400;0,700;1,400&family=Arimo:wght@400;700&display=swap">
<style>
:root{
  --orange:#b4551b;
  --orange-dark:#9a4313;
  --green:#2f9a48;
  --green-soft:#5ea94a;
  --lime:#c9d12a;
  --grey-text:#5a5a5a;
  --body-text:#222;
  --line:#dcdcdc;
  --band:#f1f1f1;
}
*{box-sizing:border-box;margin:0;padding:0}
html,body{width:1200px;height:1035px;overflow:hidden;background:#fff}
body{font-family:"PT Sans",sans-serif;color:var(--body-text);position:relative}
.site-header{position:absolute;left:0;top:0;width:1200px;height:197px;background:linear-gradient(#fff 55%,#ececec)}
.brand{position:absolute;left:110px;top:100px;display:flex;align-items:center;gap:10px}
.brand-dot{width:34px;height:34px;border-radius:50%;background:var(--green)}
.brand-name{font-family:"Play",sans-serif;font-size:36px;color:var(--orange);font-weight:400;letter-spacing:-.5px}
.main-nav{position:absolute;left:567px;top:0;display:flex;height:56px}
.main-nav a{font-family:"Play",sans-serif;font-size:15px;color:var(--grey-text);text-decoration:none;display:flex;align-items:center;padding:0 18px;border-right:1px solid var(--line);height:56px}
.main-nav a:first-child{border-left:1px solid var(--line);border-top:3px solid var(--orange);color:var(--green);padding:0 20px}
.quick-links{position:absolute;top:96px;left:425px;width:671px;height:80px}
.quick-link{position:absolute;display:flex;align-items:center;gap:12px;font-family:"Play",sans-serif;color:var(--grey-text)}
.quick-link .title{font-size:17px}
.quick-link .sub{font-size:14px}
.hero{position:absolute;left:107px;top:222px;width:990px;height:265px;border:2px solid #e4e4e4;background:#fff}
.hero-photo{position:absolute;left:8px;top:8px;width:355px;height:247px;background:linear-gradient(180deg,#fff 0%,#cfd8c4 55%,#8f9c80 80%,#fff 100%)}
.hero-lead{position:absolute;left:385px;top:24px;width:560px;font-family:"Play",sans-serif;font-size:24px;line-height:37px;color:#777}
.hero-lead em{font-style:normal;color:var(--orange);font-size:28px}
.hero-quote{position:absolute;left:385px;top:125px;width:570px;text-align:center;font-family:"Arimo",sans-serif;font-weight:700;font-variant:small-caps;font-size:26px;line-height:32px;color:var(--green-soft)}
.hero-quote span{color:var(--lime)}
.slider-dots{position:absolute;right:22px;bottom:22px;display:flex;gap:7px}
.slider-dots i{width:26px;height:22px;background:linear-gradient(#f4dca0,#d9a95c);border-radius:2px}
.slider-dots i.on{background:linear-gradient(#f0c010,#b4551b)}
.intro{position:absolute;left:107px;top:513px;width:700px;font-size:12.5px;line-height:15px;letter-spacing:.2px}
.intro p{margin-bottom:14px}
.intro .callout{color:var(--green-soft);font-weight:700;font-size:13px}
.benefits{list-style:none;margin:0 0 14px 12px;font-style:italic}
.benefits li{display:flex;align-items:center;gap:10px;height:14.6px}
.panel{position:absolute;left:837px;width:260px;border:1px solid #ddd;border-radius:14px;background:linear-gradient(#fff,#f6f6f6);box-shadow:0 2px 3px rgba(0,0,0,.12)}
.login{top:511px;height:156px;padding:14px 19px}
.login h2{font-family:"Arimo",sans-serif;font-size:21px;color:var(--orange);margin-bottom:10px}
.login h2 span{color:var(--green)}
.field{display:block;width:222px;height:25px;border:1px solid #ccc;background:#fff;font-size:13px;color:#444;padding:3px 7px;margin-bottom:8px}
.login-btn{float:right;margin-top:1px;width:82px;height:24px;border:none;background:linear-gradient(#d47a2a,var(--orange-dark));color:#fff;font-family:"Arimo",sans-serif;font-weight:700;font-size:14px}
.testimonial{top:690px;height:143px;padding:30px 22px 0 22px;font-family:"Arimo",sans-serif;font-size:13.5px;line-height:17px;color:#444}
.testimonial time{display:block;margin-top:7px;font-size:12px;color:var(--orange)}
.testimonial .tail{position:absolute;left:196px;bottom:-16px}
.author{position:absolute;right:104px;top:853px;font-family:"Arimo",sans-serif;font-size:15px}
.author b{color:var(--green)}
.site-footer{position:absolute;left:0;top:912px;width:1200px;height:123px;background:linear-gradient(#ececec,#fff 60%)}
.copyright{position:absolute;left:108px;top:23px;font-size:13px;line-height:16px;color:#444}
.footer-brand{position:absolute;right:104px;top:23px;display:flex;align-items:center;gap:12px}
.footer-brand .brand-dot{width:62px;height:62px;background:#bdbdbd}
.footer-brand .brand-name{color:#a8a8a8;font-size:42px}
</style>
</head>
<body>
<header class="site-header">
  <div class="brand"><span class="brand-dot"></span><span class="brand-name">lumora australia</span></div>
  <nav class="main-nav">
    <a href="#">Home</a><a href="#">How it works?</a><a href="#">About Us</a><a href="#">Testimonials</a><a href="#">Contact Us</a>
  </nav>
  <div class="quick-links">
    <a class="quick-link" style="left:0;top:0">
      <svg width="90" height="80" viewBox="0 0 90 80"><ellipse cx="38" cy="40" rx="36" ry="26" fill="#cfe9f5" stroke="#9cc7dc"/><path d="M30 62 L26 76 L44 64Z" fill="#cfe9f5"/><path d="M52 32 L78 8 L84 14 L58 38Z" fill="#f0a030"/><path d="M52 32 L48 42 L58 38Z" fill="#e8c9a0"/></svg>
      <span class="title">Get a quote</span>
    </a>
    <a class="quick-link" style="left:218px;top:0">
      <svg width="82" height="80" viewBox="0 0 82 80"><g fill="#4fb848"><rect x="8" y="56" width="10" height="16"/><rect x="24" y="46" width="10" height="26"/><rect x="40" y="34" width="10" height="38"/><rect x="56" y="18" width="10" height="54"/></g><polyline points="4,60 22,40 34,48 64,10" fill="none" stroke="#b02020" stroke-width="3"/></svg>
      <span><span class="title">Energy Raters</span><br><span class="sub">Add your busines</span></span>
    </a>
    <a class="quick-link" style="left:462px;top:0">
      <svg width="96" height="80" viewBox="0 0 96 80"><rect x="4" y="6" width="84" height="66" fill="#fff" stroke="#bbb"/><g stroke="#ddd"><line x1="4" y1="16" x2="88" y2="16"/><line x1="4" y1="26" x2="88" y2="26"/><line x1="4" y1="36" x2="88" y2="36"/><line x1="4" y1="46" x2="88" y2="46"/><line x1="4" y1="56" x2="88" y2="56"/><line x1="14" y1="6" x2="14" y2="72"/><line x1="40" y1="6" x2="40" y2="72"/><line x1="64" y1="6" x2="64" y2="72"/></g><rect x="4" y="6" width="84" height="10" fill="#dbe6f4"/></svg>
      <span class="title">Active Job Board</span>
    </a>
  </div>
</header>

<section class="hero">
  <div class="hero-photo" role="img" aria-label="Stacks of banknote cubes rising like a bar chart"></div>
  <p class="hero-lead">It’s <em>FREE</em>, <em>FAST</em> and <em>EASY</em> to use and you get the best price and turnaround time that suits you!!</p>
  <p class="hero-quote">“Get the best priced quotes for your <span>energy ratings”</span></p>
  <div class="slider-dots"><i class="on"></i><i></i><i></i><i></i><i></i></div>
</section>

<main class="intro">
  <p>Lumora australia is Australia’s leading professional energy rating consultancy firm specializing in large scaled residential and commercial energy rating logistics.</p>
  <p>We have professional and accredited energy raters in all States and Territories ready and waiting to provide quotes for and perform &nbsp;your energy rating jobs!</p>
  <p class="callout">It’s Free, Fast and Easy to use and you get the best price and turnaround time that suits you!!</p>
  <p>Register with us, upload your job and specifications, and sit back and watch as energy raters provide quotes for your work!</p>
  <ul class="benefits">
    <li><svg width="14" height="11" viewBox="0 0 14 11"><path d="M1 6 L5 10 L13 1" fill="none" stroke="#3a9a3a" stroke-width="2.4"/></svg>Get the best priced quotes for your energy ratings</li>
    <li><svg width="14" height="11" viewBox="0 0 14 11"><path d="M1 6 L5 10 L13 1" fill="none" stroke="#3a9a3a" stroke-width="2.4"/></svg>Save time by listing a job to get many quotes</li>
    <li><svg width="14" height="11" viewBox="0 0 14 11"><path d="M1 6 L5 10 L13 1" fill="none" stroke="#3a9a3a" stroke-width="2.4"/></svg>Monitor your jobs and quotes on your own job board</li>
    <li><svg width="14" height="11" viewBox="0 0 14 11"><path d="M1 6 L5 10 L13 1" fill="none" stroke="#3a9a3a" stroke-width="2.4"/></svg>Be notified via email of all new quotes as they come in</li>
    <li><svg width="14" height="11" viewBox="0 0 14 11"><path d="M1 6 L5 10 L13 1" fill="none" stroke="#3a9a3a" stroke-width="2.4"/></svg>Be able to specify your desired turnaround times</li>
    <li><svg width="14" height="11" viewBox="0 0 14 11"><path d="M1 6 L5 10 L13 1" fill="none" stroke="#3a9a3a" stroke-width="2.4"/></svg>Accessible anytime and anywhere</li>
    <li><svg width="14" height="11" viewBox="0 0 14 11"><path d="M1 6 L5 10 L13 1" fill="none" stroke="#3a9a3a" stroke-width="2.4"/></svg>Choose a deadline for energy raters to supply quotes</li>
    <li><svg width="14" height="11" viewBox="0 0 14 11"><path d="M1 6 L5 10 L13 1" fill="none" stroke="#3a9a3a" stroke-width="2.4"/></svg>Have access to many qualified energy raters in your state all quoting for your work</li>
    <li><svg width="14" height="11" viewBox="0 0 14 11"><path d="M1 6 L5 10 L13 1" fill="none" stroke="#3a9a3a" stroke-width="2.4"/></svg>Be able to track your jobs and pay online</li>
    <li><svg width="14" height="11" viewBox="0 0 14 11"><path d="M1 6 L5 10 L13 1" fill="none" stroke="#3a9a3a" stroke-width="2.4"/></svg>Provide feedback on energy raters</li>
  </ul>
  <p>Its totally free to be registered with us and there is no obligations or hidden catches! &nbsp;So if you wish to utilise the amazing opportunity register now! &nbsp;This new website will be going live on the (insert date) so be ready to save some money!</p>
</main>

<aside class="panel login">
  <h2>User <span>Login</span></h2>
  <div class="field">Username</div>
  <div class="field">Password</div>
  <button class="login-btn">LOGIN</button>
</aside>

<aside class="panel testimonial">
  <blockquote>"Lorem ipsum dolor sit amet, consectetur adipisicing elit, sed do eiusmod tempor incididu"</blockquote>
  <time>03.03.2010 10:30:00</time>
  <svg class="tail" width="36" height="17" viewBox="0 0 36 17"><path d="M0 0 L18 16 L36 0Z" fill="#f6f6f6" stroke="#ddd"/><rect x="1" y="0" width="34" height="2" fill="#f6f6f6"/></svg>
</aside>
<p class="author"><b>Marten</b>, manager</p>

<footer class="site-footer">
  <p class="copyright">Copyright 2010 (C) www.lumoraaustralia.com<br>Allrights reserved</p>
  <div class="footer-brand"><span class="brand-dot"></span><span class="brand-name">lumora australia</span></div>
</footer>
</body>
</html>
```